Buisness card

**Front Side:**

**[Your Company Logo]**
**Steadfast Upkeep Engineering**
*Keeping Your Equipment Running Smoothly*

**Contact Information:**
- **Name:** [dale Harwick
- **Title:** [owner
- **Phone:** [5073918246
- **Email:** dale@suevx.com

**Back Side:**

**Services Offered:**
- Routine Inspections
- Equipment Maintenance
- Emergency Repairs
- Consultation Services
- New installs
Tag line
Be proactive not reactive

```html
<!DOCTYPE html>
<html lang="en">
<head>
<meta charset="utf-8">
<title>Steadfast Upkeep Engineering – Business Card</title>
<link rel="stylesheet" href="https://fonts.googleapis.com/css2?family=Montserrat:wght@400;500;600;700;800&display=swap">
<style>
  :root {
    --navy: #082461;
    --navy-deep: #051a4a;
    --cyan: #1fb8f0;
    --blue: #1a73f0;
    --white: #ffffff;
    --ink: #111a2e;
    --stage: #2a2a2a;
  }
  * { box-sizing: border-box; margin: 0; padding: 0; }
  html, body { width: 1200px; height: 800px; overflow: hidden; }
  body {
    background: var(--stage);
    font-family: "Montserrat", sans-serif;
    display: flex;
    align-items: center;
    justify-content: center;
    gap: 40px;
  }
  .card {
    position: relative;
    width: 540px;
    height: 308px;
    border-radius: 22px;
    overflow: hidden;
  }

  /* Front */
  .card-front {
    background: linear-gradient(135deg, #0b2c72 0%, var(--navy) 50%, var(--navy-deep) 100%);
    color: var(--white);
  }
  .brand {
    position: absolute;
    top: 30px;
    left: 28px;
    display: flex;
    align-items: center;
    gap: 10px;
  }
  .brand-dot {
    width: 34px;
    height: 34px;
    border-radius: 50%;
    background: var(--cyan);
    flex: none;
  }
  .brand-name {
    font-weight: 700;
    font-size: 13px;
    line-height: 1.2;
    color: var(--white);
  }
  .brand-tag {
    font-size: 7.5px;
    font-weight: 600;
    letter-spacing: 0.5px;
    margin-top: 2px;
  }
  .person {
    position: absolute;
    top: 30px;
    right: 30px;
    text-align: right;
  }
  .person-name { font-weight: 800; font-size: 24px; letter-spacing: -0.3px; }
  .person-title { font-weight: 500; font-size: 12px; letter-spacing: 1.5px; }
  .company {
    position: absolute;
    left: 28px;
    top: 150px;
  }
  .company-main {
    font-weight: 800;
    font-size: 27px;
    color: var(--cyan);
    letter-spacing: 0.5px;
    line-height: 1;
  }
  .company-sub {
    font-weight: 600;
    font-size: 11.5px;
    color: var(--cyan);
    letter-spacing: 0.8px;
    margin-top: 4px;
  }
  .company-slogan {
    font-size: 12.5px;
    font-weight: 500;
    margin-top: 6px;
  }
  .contact {
    position: absolute;
    left: 28px;
    bottom: 26px;
    list-style: none;
  }
  .contact li {
    display: flex;
    align-items: center;
    gap: 10px;
    font-size: 15px;
    font-weight: 500;
    margin-top: 7px;
  }
  .contact-icon {
    width: 22px;
    height: 22px;
    border-radius: 5px;
    background: var(--blue);
    display: flex;
    align-items: center;
    justify-content: center;
    flex: none;
  }

  /* Back */
  .card-back { background: var(--white); color: var(--ink); }
  .services {
    position: absolute;
    top: 28px;
    left: 250px;
  }
  .services-title {
    font-weight: 800;
    font-size: 21px;
    color: var(--navy);
    line-height: 1.05;
    letter-spacing: 0.5px;
  }
  .services-list {
    list-style: none;
    margin-top: 10px;
  }
  .services-list li {
    position: relative;
    padding-left: 16px;
    font-size: 13px;
    font-weight: 500;
    line-height: 1.6;
  }
  .services-list li::before {
    content: "";
    position: absolute;
    left: 0;
    top: 8px;
    width: 6px;
    height: 6px;
    border-radius: 50%;
    background: var(--blue);
  }
  .back-brand {
    position: absolute;
    left: 36px;
    top: 60px;
    width: 170px;
    display: flex;
    flex-direction: column;
    align-items: center;
    gap: 10px;
    text-align: center;
  }
  .back-brand-dot {
    width: 90px;
    height: 90px;
    border-radius: 50%;
    background: var(--navy);
  }
  .back-brand-name {
    font-weight: 700;
    font-size: 13px;
    color: var(--navy);
    line-height: 1.2;
  }
  .band-low {
    position: absolute;
    left: 0;
    top: 262px;
    width: 210px;
    height: 20px;
    background: var(--blue);
  }
  .tagline-band {
    position: absolute;
    left: 210px;
    right: 0;
    top: 218px;
    height: 36px;
    background: linear-gradient(90deg, var(--blue) 0%, var(--blue) 82%, var(--cyan) 82%, var(--cyan) 100%);
    display: flex;
    align-items: center;
    padding-left: 22px;
  }
  .tagline {
    font-weight: 700;
    font-size: 15px;
    color: var(--white);
    letter-spacing: 0.8px;
    white-space: nowrap;
  }
</style>
</head>
<body>

  <section class="card card-front" aria-label="Business card front">
    <div class="brand">
      <span class="brand-dot"></span>
      <div>
        <p class="brand-name">Steadfast Upkeep Engineering</p>
        <p class="brand-tag">BE PROACTIVE NOT REACTIVE</p>
      </div>
    </div>

    <div class="person">
      <p class="person-name">dale Harwick</p>
      <p class="person-title">FOUNDER</p>
    </div>

    <div class="company">
      <p class="company-main">STEADFAST</p>
      <p class="company-sub">UPKEEP ENGINEERING</p>
      <p class="company-slogan">Keeping Your Equipment Running Smoothly</p>
    </div>

    <ul class="contact">
      <li>
        <span class="contact-icon">
          <svg width="13" height="13" viewBox="0 0 24 24" aria-hidden="true">
            <path fill="#fff" d="M6.6 10.8a15.5 15.5 0 0 0 6.6 6.6l2.2-2.2c.3-.3.7-.4 1-.2 1.1.4 2.3.6 3.6.6.6 0 1 .4 1 1V20c0 .6-.4 1-1 1A17 17 0 0 1 3 4c0-.6.4-1 1-1h3.5c.6 0 1 .4 1 1 0 1.3.2 2.5.6 3.6.1.3 0 .7-.2 1z"/>
          </svg>
        </span>
        5073918246
      </li>
      <li>
        <span class="contact-icon">
          <svg width="13" height="13" viewBox="0 0 24 24" aria-hidden="true">
            <path fill="#fff" d="M2 21 23 12 2 3v7l15 2-15 2z"/>
          </svg>
        </span>
        dale@suevx.com
      </li>
    </ul>
  </section>

  <section class="card card-back" aria-label="Business card back">
    <div class="band-low"></div>

    <div class="services">
      <h2 class="services-title">SERVICES<br>OFFERED:</h2>
      <ul class="services-list">
        <li>Routine Inspections</li>
        <li>Equipment Maintenance</li>
        <li>Emergency Repairs</li>
        <li>Consultation Services</li>
        <li>New installs</li>
      </ul>
    </div>

    <div class="back-brand">
      <span class="back-brand-dot"></span>
      <p class="back-brand-name">Steadfast Upkeep Engineering</p>
    </div>

    <div class="tagline-band">
      <p class="tagline">BE PROACTIVE NOT REACTIVE</p>
    </div>
  </section>

</body>
</html>
```